Cleaning Company needs a new business card design

Hi, We are looking for new business card designs to update with our latest logo and company information.
We would like to see designs using the colours:
Royal Blue #4169E1 - this is our company colour so this has to be in there. Please feel free to experiment with other colours.
Must include:
Front of business card:
Logo
Back of the business card:
0800 529 6081
07438 915 702
Email: info@pkrtidyhomes.co.uk
Web: www.pkrtidyhomes.co.uk
Services:
End of Tenancy
Carpet & Upholstery
Regular & One Off
all work fully insured.
The front of the business card with the logo can be made to look raised print. The blue man to be a shiny finish.
The business card needs to be presented in a matt finish
The business must be in the following styles:
Standard Square with rounded corners.
Thank you to all that take part in this.
Target Market(s)
Men and Women of different ages in the UK.
Industry/Entity Type
House Cleaning
Contact Information for Business Card
Front of business card:
Logo
0800 529 6081
07438 915 702
Email: pkrtidy@mailbox-demo.co.uk
Services:
End of Tenancy
Carpet & Upholstery
Regular & One Off
all work fully insured.

```html
<!DOCTYPE html>
<html lang="en">
<head>
<meta charset="utf-8">
<title>PKR Tidy Homes – Business Card</title>
<link href="https://fonts.googleapis.com/css2?family=Ubuntu:wght@300;500;700&display=swap" rel="stylesheet">
<style>
  :root {
    --backdrop: #5e5b58;
    --card-white: #ffffff;
    --brand-navy: #1f44a0;
    --brand-royal: #2e4a9b;
    --ink-light: #ffffff;
  }
  * { box-sizing: border-box; margin: 0; padding: 0; }
  html, body {
    width: 1200px; height: 1200px; overflow: hidden;
    background: var(--backdrop);
    font-family: "Ubuntu", sans-serif;
  }
  .stage { position: relative; width: 1200px; height: 1200px; }
  .card {
    position: absolute; left: 262px; width: 676px; height: 406px;
    border-radius: 34px;
  }
  .card--front { top: 154px; background: var(--card-white); }
  .card--back { top: 640px; background: var(--brand-royal); }

  .brand {
    position: absolute; left: 50%; top: 50%;
    transform: translate(-50%, -50%);
    display: flex; align-items: center; gap: 12px;
    white-space: nowrap;
  }
  .brand__dot {
    width: 26px; height: 26px; border-radius: 50%;
    background: var(--brand-navy);
  }
  .brand__name {
    font-weight: 700; font-size: 38px; letter-spacing: -0.5px;
    color: var(--brand-navy);
  }

  .contact {
    position: absolute; left: 374px; top: 255px;
    list-style: none;
  }
  .contact__item {
    display: flex; align-items: center; gap: 10px;
    height: 27px;
    color: var(--ink-light);
    font-weight: 300; font-size: 17.5px; letter-spacing: 0.2px;
  }
  .contact__icon { width: 20px; height: 20px; flex: none; }
</style>
</head>
<body>
<main class="stage">
  <section class="card card--front" aria-label="Card front">
    <div class="brand">
      <span class="brand__dot"></span>
      <span class="brand__name">PKR Tidy Homes Limited</span>
    </div>
  </section>

  <section class="card card--back" aria-label="Card back">
    <ul class="contact">
      <li class="contact__item">
        <svg class="contact__icon" viewBox="0 0 20 20" aria-hidden="true">
          <circle cx="10" cy="10" r="10" fill="#fff"/>
          <path d="M6.3 5.2c.5-.4 1.1-.3 1.4.2l1 1.6c.3.5.1 1-.3 1.3l-.6.4c.5 1.3 1.4 2.3 2.6 3l.5-.6c.3-.4.9-.5 1.3-.2l1.6 1c.5.3.6 1 .2 1.4l-.8.9c-.5.5-1.3.6-2 .3-2.6-1.2-4.5-3.2-5.6-5.8-.3-.7-.1-1.5.4-2z" fill="var(--brand-royal)"/>
        </svg>
        <span>0800 529 6081</span>
      </li>
      <li class="contact__item">
        <svg class="contact__icon" viewBox="0 0 20 20" aria-hidden="true">
          <circle cx="10" cy="10" r="10" fill="#fff"/>
          <rect x="7" y="4.5" width="6" height="11" rx="1.2" fill="var(--brand-royal)"/>
          <rect x="8" y="6" width="4" height="7" fill="#fff"/>
        </svg>
        <span>07438 915 702</span>
      </li>
      <li class="contact__item">
        <svg class="contact__icon" viewBox="0 0 20 20" aria-hidden="true">
          <circle cx="10" cy="10" r="10" fill="#fff"/>
          <rect x="4.5" y="6.5" width="11" height="7.5" rx="1" fill="var(--brand-royal)"/>
          <path d="M5 7l5 4 5-4M5 13.5l3.5-3.5M15 13.5l-3.5-3.5" stroke="#fff" stroke-width="0.9" fill="none"/>
        </svg>
        <span>info@pkrtidyhomes.co.uk</span>
      </li>
      <li class="contact__item">
        <svg class="contact__icon" viewBox="0 0 20 20" aria-hidden="true">
          <circle cx="10" cy="10" r="10" fill="#fff"/>
          <g stroke="var(--brand-royal)" stroke-width="1" fill="none">
            <circle cx="10" cy="10" r="5.5"/>
            <ellipse cx="10" cy="10" rx="2.4" ry="5.5"/>
            <path d="M4.5 10h11M5.3 7.3h9.4M5.3 12.7h9.4"/>
          </g>
        </svg>
        <span>www.pkrtidyhomes.co.uk</span>
      </li>
    </ul>
  </section>
</main>
</body>
</html>
```